High end business card design for custom homebuilding company

Looking for a high end business card design that is unique and elegant. Can use embossing, foil printing, laser die cutting, or any high end printing technique or high end paper. Will upload current design so you can see the logo and what we are using currently, but we want something more unique and elegant. I included our logo to help with design.

Target Market(s)

High end custom home buyers of $1.5 million plus homes. Also real estate developers of high end communities.

Industry/Entity Type

Business

Contact Information for Business Card

Double sided. We want something very elegant and expensive looking. We are looking to incorporate a combination of perhaps linen paper or a high end paper, with foil stamping or embossing/debossing to make the card look unique, but still elegant. We tend to use blacks and golds, but are open to any ideas. Looking for creative and unique design.

Colors

Designer to choose colors to be used in the design.

Requirements
Must have
• High end, elegant look. Can use foil, embossing, or high end papers like linen. We want to make the card unique and interesting, but elegant and expensive looking.
Nice to have
• I am including just some cards I saw that looked interesting for one reason or another. I like a clean elegant design and like both the clean white style, and the blacks. So not sure if we want a black design or white. Would like to see both.

```html
<!DOCTYPE html>
<html lang="en">
<head>
<meta charset="utf-8">
<title>Brightpeak Custom Homes – Business Card</title>
<link rel="stylesheet" href="https://fonts.googleapis.com/css2?family=Open+Sans:wght@400&family=Arimo:wght@700&display=swap">
<style>
  :root {
    --backdrop: #e8e5e1;
    --card: #2b2a29;
    --gold: #c9a46a;
    --tab: #4a4a4b;
    --ink-strong: #8e8e8e;
    --ink: #9c9c9c;
    --ink-soft: #7a7a7a;
    --follow: #c4c4c4;
    --social: #7d7d7d;
    --mark-faint: #3c3c3d;
  }
  * { margin: 0; padding: 0; box-sizing: border-box; }
  html, body { width: 1142px; height: 1200px; overflow: hidden; background: var(--backdrop); }
  .stage { position: relative; width: 1200px; height: 1261px; transform: scale(0.9517); transform-origin: 0 0; }

  .card { position: absolute; background: var(--card); width: 837px; height: 492px; box-shadow: 0 6px 18px rgba(0,0,0,.18); }
  .card--front { left: 125px; top: 113px; }
  .card--back { left: 246px; top: 676px; }

  .edge-gold { position: absolute; width: 13px; background: var(--gold); }
  .edge-tab { position: absolute; width: 35px; background: var(--tab); top: 137px; height: 217px; }
  .card--front .edge-gold { left: 0; }
  .card--front .edge-tab { left: 0; }
  .card--back .edge-gold { right: 0; }
  .card--back .edge-tab { right: 0; }
  .edge-gold.top { top: 0; height: 137px; }
  .edge-gold.bottom { bottom: 0; height: 138px; }

  .brand { position: absolute; left: 107px; top: 200px; display: flex; align-items: center; gap: 18px; }
  .brand-dot { width: 44px; height: 44px; border-radius: 50%; background: var(--gold); flex: none; }
  .brand-name { font-family: "Open Sans", sans-serif; font-weight: 400; font-size: 40px; line-height: 1; color: var(--ink-soft); letter-spacing: 1px; white-space: nowrap; }
  .brand-url { position: absolute; left: 107px; top: 292px; font-family: "Open Sans", sans-serif; font-size: 28px; color: var(--ink-soft); letter-spacing: 4.6px; white-space: nowrap; }

  .back-mark { position: absolute; left: 60px; top: 150px; width: 230px; height: 210px; border-radius: 50%; background: var(--mark-faint); }

  .person { position: absolute; left: 382px; top: 62px; font-family: "Open Sans", sans-serif; font-weight: 400; font-size: 33px; color: var(--ink-strong); letter-spacing: -0.5px; }
  .contacts { position: absolute; left: 338px; top: 152px; list-style: none; }
  .contacts li { display: flex; align-items: center; gap: 17px; margin-bottom: 12px; }
  .contacts .icon { width: 27px; height: 27px; flex: none; }
  .contacts .lines { font-family: "Open Sans", sans-serif; font-size: 24px; line-height: 27px; color: var(--ink); white-space: nowrap; }

  .follow { position: absolute; left: 376px; top: 390px; width: 200px; }
  .follow-label { font-family: "Arimo", sans-serif; font-weight: 700; font-size: 17px; color: var(--follow); margin-left: 24px; }
  .social { display: flex; gap: 12px; margin-top: 7px; }
  .social span { width: 30px; height: 30px; background: var(--social); border-radius: 3px; }
</style>
</head>
<body>
<div class="stage">

  <section class="card card--front">
    <div class="edge-gold top"></div>
    <div class="edge-tab"></div>
    <div class="edge-gold bottom"></div>
    <div class="brand">
      <span class="brand-dot"></span>
      <span class="brand-name">Brightpeak Custom Homes</span>
    </div>
    <div class="brand-url">www.brightpeakhomes.com.au</div>
  </section>

  <section class="card card--back">
    <div class="edge-gold top"></div>
    <div class="edge-tab"></div>
    <div class="edge-gold bottom"></div>

    <div class="back-mark" role="img" aria-label="Large faint company mark"></div>

    <h1 class="person">DUMMY NAME</h1>
    <ul class="contacts">
      <li>
        <svg class="icon" viewBox="0 0 28 28" aria-hidden="true">
          <circle cx="14" cy="14" r="13" fill="var(--gold)"/>
          <path d="M9 7.5c1-.6 1.8 0 2.4 1l1 2c.4.8.1 1.4-.6 1.9l-.6.4c.7 1.8 2 3.2 3.8 4l.5-.6c.5-.7 1.2-.9 2-.5l2 1c1 .5 1.5 1.4.9 2.3-1 1.6-2.8 2-4.6 1.200-3.3-1.5-5.6-3.8-7-7.1C8 10.3 8 8.3 9 7.5z" fill="var(--card)"/>
        </svg>
        <div class="lines">00 0000 0000<br>00 0000 0000</div>
      </li>
      <li>
        <svg class="icon" viewBox="0 0 28 28" aria-hidden="true">
          <rect x="1" y="1" width="26" height="26" rx="4" fill="var(--gold)"/>
          <circle cx="14" cy="14" r="8" fill="none" stroke="var(--card)" stroke-width="1.6"/>
          <ellipse cx="14" cy="14" rx="3.5" ry="8" fill="none" stroke="var(--card)" stroke-width="1.4"/>
          <path d="M6 14h16M7.5 10h13M7.5 18h13" stroke="var(--card)" stroke-width="1.3"/>
        </svg>
        <div class="lines">hello@brightpeak.com.au<br>www.brightpeakhomes.com.au</div>
      </li>
      <li>
        <svg class="icon" viewBox="0 0 28 28" aria-hidden="true">
          <path d="M14 2a9 9 0 0 1 9 9c0 6.5-9 15-9 15S5 17.5 5 11a9 9 0 0 1 9-9z" fill="var(--gold)"/>
          <circle cx="14" cy="11" r="3.6" fill="var(--card)"/>
        </svg>
        <div class="lines">unit 4 18-22 Harlow Street,<br>Bentley, WA 6102</div>
      </li>
    </ul>

    <div class="follow">
      <div class="follow-label">Follow Us On:</div>
      <div class="social">
        <span role="img" aria-label="Social network link"></span>
        <span role="img" aria-label="Social network link"></span>
        <span role="img" aria-label="Social network link"></span>
        <span role="img" aria-label="Social network link"></span>
        <span role="img" aria-label="Video channel link"></span>
      </div>
    </div>
  </section>

</div>
</body>
</html>
```